KWT Contracting services . Building and maintenance services, optic fibre installation

Business cards and logo design.I need a logo that I can use on business cards ,workwear and on my vehicles. I would like the KWT to be the main or larger text and contracting services to be the smaller or less important text.I like monograms, modern designs and repeating patterns symbols. I am also a Gemini and my favourite number is 22 so if this can be any inspiration to help with the design. Am thinking of the using German flag colours as a his is my family’s heritage. And the other 2 main colours I wear is black and white.But any ideas are appreciated.I do not need a design that is trade specific but a design that could be used for any business.

Target Market(s)

General public

Contact Information for Business Card

KWT Contracting Services ( front of business card)

(Back of business card)
Milo Brackwood
0471539264
Maintenance services
Optic fibre and data installation

Logo Text

Logo can just be pattern or monogram or incorporate KWT . I like the gemini star sign and the number 22

Colors
ec1f27
000000
fbee3e
ffffff

Requirements
Must have
• Logo and KWT Contracting Services on the front of business card
Nice to have
• Possible use of German flag colours.
• Modern design.
• Design to be able to be used on black or white background as I want to put it on clothing

```html
<!DOCTYPE html>
<html lang="en">
<head>
<meta charset="utf-8">
<title>KWT Contracting Services – Business Card</title>
<link rel="stylesheet" href="https://fonts.googleapis.com/css2?family=Orbitron:wght@600;700&family=Ubuntu:wght@400;500&display=swap">
<style>
  :root {
    --stage: #5d5e59;
    --card: #1d1b1c;
    --yellow: #fbd600;
    --red: #ec1f27;
    --white: #ffffff;
  }
  * { box-sizing: border-box; margin: 0; padding: 0; }
  html, body {
    width: 1200px;
    height: 1076px;
    overflow: hidden;
    background: var(--stage);
  }
  .stage {
    position: relative;
    width: 1200px;
    height: 1076px;
  }
  .card {
    position: absolute;
    background: var(--card);
    border-radius: 26px;
    overflow: hidden;
  }

  /* Front */
  .card-front {
    left: 110px;
    top: 560px;
    width: 580px;
    height: 330px;
    display: flex;
    flex-direction: column;
    align-items: center;
    justify-content: center;
    gap: 14px;
  }
  .brand-name {
    font-family: "Orbitron", sans-serif;
    font-weight: 700;
    color: var(--yellow);
    letter-spacing: 6px;
    line-height: 1;
  }
  .card-front .brand-name { font-size: 118px; }
  .brand-tagline {
    font-family: "Orbitron", sans-serif;
    font-weight: 600;
    color: var(--yellow);
    text-transform: uppercase;
    white-space: nowrap;
    line-height: 1;
  }
  .card-front .brand-tagline {
    font-size: 29px;
    letter-spacing: 2.5px;
  }

  /* Back */
  .card-back {
    left: 720px;
    top: 80px;
    width: 330px;
    height: 580px;
    padding: 44px 34px 40px 38px;
    display: flex;
    flex-direction: column;
  }
  .card-back .brand {
    align-self: flex-end;
    text-align: right;
  }
  .card-back .brand-name {
    font-size: 72px;
    letter-spacing: 4px;
  }
  .card-back .brand-tagline {
    margin-top: 10px;
    font-size: 15.5px;
    letter-spacing: 1.2px;
  }
  .contact {
    margin-top: 56px;
    font-family: "Ubuntu", sans-serif;
    color: var(--yellow);
  }
  .person-name {
    font-size: 33px;
    font-weight: 500;
    line-height: 1.08;
    letter-spacing: 1.5px;
    text-transform: uppercase;
    text-align: center;
  }
  .phone {
    margin-top: 18px;
    display: flex;
    align-items: center;
    gap: 12px;
    font-size: 25px;
    letter-spacing: 2px;
  }
  .phone-icon { width: 18px; height: 22px; flex: none; }
  .services {
    margin-top: auto;
    list-style: none;
    font-family: "Ubuntu", sans-serif;
    font-size: 13px;
    letter-spacing: 0.6px;
    color: var(--yellow);
    text-transform: uppercase;
    line-height: 1.9;
  }
  .services li::before { content: "-"; }
</style>
</head>
<body>
<main class="stage">

  <section class="card card-back" aria-label="Business card back">
    <div class="brand">
      <div class="brand-name">KWT</div>
      <div class="brand-tagline">Contracting Services</div>
    </div>
    <div class="contact">
      <p class="person-name">Milo<br>Brackwood</p>
      <p class="phone">
        <svg class="phone-icon" viewBox="0 0 18 22" aria-hidden="true">
          <path d="M4 1 L8 1 L8 6 L5.5 7.5 C6 11 7.5 14 10 16.5 L12.5 15 L16 18.5 L13 21 C6 19 1.5 11 2 3 Z" fill="var(--red)"/>
        </svg>
        <span>0471 539 264</span>
      </p>
    </div>
    <ul class="services">
      <li>Maintenance services</li>
      <li>Optic fibre and data installation</li>
    </ul>
  </section>

  <section class="card card-front" aria-label="Business card front">
    <div class="brand-name">KWT</div>
    <div class="brand-tagline">Contracting Services</div>
  </section>

</main>
</body>
</html>
```